PulseLedgerPro.Com PowerPoint

I need a PowerPoint layout for my presentations. My business is called PulseLedgerPro.Com - my presentations teach cardiologists how to document their procedures and visits and teaches them how to bill accurately for them.

Industry/Entity Type

Business

Requirements
Must have
• the logo should be subtly there on each page - perhaps as a watermark? I'm really not creative; please help.

```html
<!DOCTYPE html>
<html lang="en">
<head>
<meta charset="utf-8">
<title>PulseLedgerPro.Com – Title Slide</title>
<link href="https://fonts.googleapis.com/css2?family=Exo+2:wght@600;700;800&family=Open+Sans:wght@400&display=swap" rel="stylesheet">
<style>
  :root {
    --brand-red: #c21e24;
    --deep-blue: #1f63cf;
    --sky-blue: #8cc0ee;
    --pale-blue: #dcebf9;
    --title-grey: #5b5b5b;
    --body-grey: #5e5e5e;
    --tab-dark: #3a3a3a;
    --white: #ffffff;
  }
  html, body {
    margin: 0;
    padding: 0;
    overflow: hidden;
    background: var(--white);
  }
  .slide {
    position: relative;
    width: 1200px;
    height: 900px;
    overflow: hidden;
    background: var(--white);
  }
  .slide-art {
    position: absolute;
    inset: 0;
    width: 1200px;
    height: 900px;
  }
  .project-title {
    position: absolute;
    left: 65px;
    top: 588px;
    margin: 0;
    font-family: "Exo 2", sans-serif;
    font-weight: 800;
    font-size: 40px;
    letter-spacing: 0.5px;
    color: var(--title-grey);
  }
  .content-lines {
    position: absolute;
    left: 65px;
    top: 648px;
    margin: 0;
    padding: 0;
    list-style: none;
    font-family: "Open Sans", sans-serif;
    font-size: 24px;
    line-height: 37.5px;
    color: var(--body-grey);
  }
  .brand-mark {
    position: absolute;
    left: 693px;
    top: 660px;
    display: flex;
    align-items: center;
    gap: 16px;
  }
  .brand-dot {
    width: 56px;
    height: 56px;
    border-radius: 50%;
    background: var(--brand-red);
  }
  .brand-name {
    font-family: "Exo 2", sans-serif;
    font-weight: 700;
    font-size: 42px;
    color: var(--brand-red);
  }
  .copyright-tab {
    position: absolute;
    left: 909px;
    top: 835px;
    width: 291px;
    height: 43px;
    border-radius: 12px 0 0 12px;
    background: var(--tab-dark);
    display: flex;
    align-items: center;
    justify-content: center;
    font-family: "Exo 2", sans-serif;
    font-weight: 600;
    font-size: 21px;
    color: var(--white);
  }
</style>
</head>
<body>
<div class="slide">
  <svg class="slide-art" viewBox="0 0 800 600" preserveAspectRatio="none" aria-hidden="false">
    <defs>
      <linearGradient id="headerGlow" x1="0" y1="0" x2="1" y2="0.4">
        <stop offset="0" stop-color="var(--deep-blue)"/>
        <stop offset="0.45" stop-color="var(--sky-blue)"/>
        <stop offset="1" stop-color="var(--pale-blue)"/>
      </linearGradient>
    </defs>
    <rect class="header-photo" x="0" y="0" width="800" height="360" fill="url(#headerGlow)"
          role="img" aria-label="Medical photo: globe, heartbeat lines and a doctor in a white coat holding a stethoscope"/>
    <path class="swoosh-red" fill="var(--brand-red)"
          d="M0,115 C150,200 350,300 560,305 C660,307 740,290 800,268 L800,322 C700,348 560,362 440,352 C280,338 130,265 0,245 Z"/>
    <path class="swoosh-stripe" fill="none" stroke="var(--white)" stroke-width="5"
          d="M120,258 C280,318 440,338 560,334 C660,330 740,312 800,292"/>
    <path class="content-field" fill="var(--white)"
          d="M0,245 C130,265 280,338 440,352 C560,362 700,348 800,322 L800,600 L0,600 Z"/>
    <rect class="footer-band" x="0" y="545" width="800" height="55" fill="var(--brand-red)"/>
  </svg>

  <h1 class="project-title">PROJECT TITLE HERE</h1>
  <ul class="content-lines">
    <li>Content here, Content here</li>
    <li>Content here Content here, Content here</li>
    <li>Content here Content here</li>
  </ul>

  <div class="brand-mark">
    <span class="brand-dot"></span>
    <span class="brand-name">PulseLedgerPro.Com</span>
  </div>

  <div class="copyright-tab">COPYRIGHT TEXT HERE</div>
</div>
</body>
</html>
```